2026 Calendar Design for Construction Company

2026 Calendar for a underground utility construction company January - December 2026 all on one long page lnwarbeck.com is our website Safety Quality Production is our slogan

```html
<!DOCTYPE html>
<html lang="en">
<head>
<meta charset="utf-8">
<title>LN Warbeck 2026 Calendar</title>
<link rel="stylesheet" href="https://fonts.googleapis.com/css2?family=Poppins:wght@400;500;600;700;800;900&display=swap">
<style>
:root{
  --yellow:#f2e600;
  --ink:#000000;
  --panel:#0b0b0b;
  --band:#121210;
  --white:#ffffff;
  --paper:#ffffff;
}
*{margin:0;padding:0;box-sizing:border-box}
html,body{width:1200px;height:1200px;overflow:hidden;background:var(--paper)}
body{font-family:"Poppins",sans-serif;position:relative}
.poster{position:absolute;left:220px;top:61px;width:767px;height:1085px;background:var(--ink);overflow:hidden}
.header-band{position:absolute;left:22px;top:0;right:0;height:404px;background:var(--band)}
.hero-photo{position:absolute;left:324px;top:0;right:0;height:250px;
  background:
    linear-gradient(180deg,rgba(18,18,16,0) 60%,var(--band) 100%),
    linear-gradient(90deg,var(--band) 0%,#3a3320 25%,#6b5a2a 55%,#8a7a30 80%,#a89635 100%)}
.year{position:absolute;left:62px;top:66px;display:flex;align-items:flex-end;color:var(--yellow);
  font-weight:800;font-size:128px;line-height:.8;letter-spacing:-8px}
.year .dot{width:52px;height:52px;border-radius:50%;background:var(--yellow);margin:0 8px 30px 2px;flex:none}
.month{position:absolute;width:200px;height:158px;border:1px solid var(--yellow);border-radius:14px;background:var(--panel)}
.month h2{position:absolute;top:28px;left:0;right:0;text-align:center;color:var(--yellow);
  font-weight:500;font-size:12.5px;letter-spacing:1.6px;line-height:1}
.weekdays,.days{position:absolute;left:25px;width:150px;display:grid;grid-template-columns:repeat(7,1fr);list-style:none;text-align:center;color:var(--white)}
.weekdays{top:48px;font-size:6.5px;font-weight:600;padding-bottom:4px;border-bottom:1px solid #d8d8d8}
.days{top:69px;font-size:8px;font-weight:600;row-gap:6.2px;line-height:9px}
.s1{grid-column-start:2}.s2{grid-column-start:3}.s3{grid-column-start:4}
.s4{grid-column-start:5}.s5{grid-column-start:6}.s6{grid-column-start:7}
.c1{left:64px}.c2{left:282px}.c3{left:504px}
.r1{top:208px}.r2{top:385px}.r3{top:567px}.r4{top:745px}
.brand{position:absolute;left:66px;top:984px;color:var(--yellow);font-weight:700;font-size:15px;line-height:1;white-space:nowrap}
.divider{position:absolute;left:201px;top:959px;width:1px;height:70px;background:var(--yellow)}
.slogan{position:absolute;left:216px;top:964px;color:var(--yellow);font-weight:800;font-size:17px;line-height:20.5px}
.pill{position:absolute;top:938px;width:78px;height:18px;border:1px solid var(--yellow);border-radius:9px;
  color:var(--yellow);font-size:9px;text-align:center;line-height:16px}
.contact-pill{left:366px}.services-pill{left:497px}
.info{position:absolute;top:966px;color:var(--yellow);font-size:9.2px;line-height:16.2px;list-style:none}
.contact{left:366px}
.services{left:505px;line-height:15.3px}
</style>
</head>
<body>
<main class="poster">
  <div class="header-band"></div>
  <div class="hero-photo" role="img" aria-label="Photo of three utility crew members in hard hats and safety vests reviewing plans at an industrial pipe site"></div>
  <h1 class="year" aria-label="2026"><span>2</span><span class="dot"></span><span>26</span></h1>

  <section class="month c1 r1"><h2>JANUARY</h2>
    <ul class="weekdays"><li>S</li><li>M</li><li>T</li><li>W</li><li>T</li><li>F</li><li>S</li></ul>
    <ol class="days"><li class="s4">1</li><li>2</li><li>3</li><li>4</li><li>5</li><li>6</li><li>7</li><li>8</li><li>9</li><li>10</li><li>11</li><li>12</li><li>13</li><li>14</li><li>15</li><li>16</li><li>17</li><li>18</li><li>19</li><li>20</li><li>21</li><li>22</li><li>23</li><li>24</li><li>25</li><li>26</li><li>27</li><li>28</li><li>29</li><li>30</li><li>31</li></ol>
  </section>
  <section class="month c2 r1"><h2>FEBRUARY</h2>
    <ul class="weekdays"><li>S</li><li>M</li><li>T</li><li>W</li><li>T</li><li>F</li><li>S</li></ul>
    <ol class="days"><li>1</li><li>2</li><li>3</li><li>4</li><li>5</li><li>6</li><li>7</li><li>8</li><li>9</li><li>10</li><li>11</li><li>12</li><li>13</li><li>14</li><li>15</li><li>16</li><li>17</li><li>18</li><li>19</li><li>20</li><li>21</li><li>22</li><li>23</li><li>24</li><li>25</li><li>26</li><li>27</li><li>28</li></ol>
  </section>
  <section class="month c3 r1"><h2>MARCH</h2>
    <ul class="weekdays"><li>S</li><li>M</li><li>T</li><li>W</li><li>T</li><li>F</li><li>S</li></ul>
    <ol class="days"><li>1</li><li>2</li><li>3</li><li>4</li><li>5</li><li>6</li><li>7</li><li>8</li><li>9</li><li>10</li><li>11</li><li>12</li><li>13</li><li>14</li><li>15</li><li>16</li><li>17</li><li>18</li><li>19</li><li>20</li><li>21</li><li>22</li><li>23</li><li>24</li><li>25</li><li>26</li><li>27</li><li>28</li><li>29</li><li>30</li><li>31</li></ol>
  </section>

  <section class="month c1 r2"><h2>APRIL</h2>
    <ul class="weekdays"><li>S</li><li>M</li><li>T</li><li>W</li><li>T</li><li>F</li><li>S</li></ul>
    <ol class="days"><li class="s3">1</li><li>2</li><li>3</li><li>4</li><li>5</li><li>6</li><li>7</li><li>8</li><li>9</li><li>10</li><li>11</li><li>12</li><li>13</li><li>14</li><li>15</li><li>16</li><li>17</li><li>18</li><li>19</li><li>20</li><li>21</li><li>22</li><li>23</li><li>24</li><li>25</li><li>26</li><li>27</li><li>28</li><li>29</li><li>30</li></ol>
  </section>
  <section class="month c2 r2"><h2>MAY</h2>
    <ul class="weekdays"><li>S</li><li>M</li><li>T</li><li>W</li><li>T</li><li>F</li><li>S</li></ul>
    <ol class="days"><li class="s5">1</li><li>2</li><li>3</li><li>4</li><li>5</li><li>6</li><li>7</li><li>8</li><li>9</li><li>10</li><li>11</li><li>12</li><li>13</li><li>14</li><li>15</li><li>16</li><li>17</li><li>18</li><li>19</li><li>20</li><li>21</li><li>22</li><li>23</li><li>24</li><li>25</li><li>26</li><li>27</li><li>28</li><li>29</li><li>30</li><li>31</li></ol>
  </section>
  <section class="month c3 r2"><h2>JUNE</h2>
    <ul class="weekdays"><li>S</li><li>M</li><li>T</li><li>W</li><li>T</li><li>F</li><li>S</li></ul>
    <ol class="days"><li class="s1">1</li><li>2</li><li>3</li><li>4</li><li>5</li><li>6</li><li>7</li><li>8</li><li>9</li><li>10</li><li>11</li><li>12</li><li>13</li><li>14</li><li>15</li><li>16</li><li>17</li><li>18</li><li>19</li><li>20</li><li>21</li><li>22</li><li>23</li><li>24</li><li>25</li><li>26</li><li>27</li><li>28</li><li>29</li><li>30</li></ol>
  </section>

  <section class="month c1 r3"><h2>JULY</h2>
    <ul class="weekdays"><li>S</li><li>M</li><li>T</li><li>W</li><li>T</li><li>F</li><li>S</li></ul>
    <ol class="days"><li class="s3">1</li><li>2</li><li>3</li><li>4</li><li>5</li><li>6</li><li>7</li><li>8</li><li>9</li><li>10</li><li>11</li><li>12</li><li>13</li><li>14</li><li>15</li><li>16</li><li>17</li><li>18</li><li>19</li><li>20</li><li>21</li><li>22</li><li>23</li><li>24</li><li>25</li><li>26</li><li>27</li><li>28</li><li>29</li><li>30</li><li>31</li></ol>
  </section>
  <section class="month c2 r3"><h2>AUGUST</h2>
    <ul class="weekdays"><li>S</li><li>M</li><li>T</li><li>W</li><li>T</li><li>F</li><li>S</li></ul>
    <ol class="days"><li class="s6">1</li><li>2</li><li>3</li><li>4</li><li>5</li><li>6</li><li>7</li><li>8</li><li>9</li><li>10</li><li>11</li><li>12</li><li>13</li><li>14</li><li>15</li><li>16</li><li>17</li><li>18</li><li>19</li><li>20</li><li>21</li><li>22</li><li>23</li><li>24</li><li>25</li><li>26</li><li>27</li><li>28</li><li>29</li><li>30</li><li>31</li></ol>
  </section>
  <section class="month c3 r3"><h2>SEPTEMBER</h2>
    <ul class="weekdays"><li>S</li><li>M</li><li>T</li><li>W</li><li>T</li><li>F</li><li>S</li></ul>
    <ol class="days"><li class="s2">1</li><li>2</li><li>3</li><li>4</li><li>5</li><li>6</li><li>7</li><li>8</li><li>9</li><li>10</li><li>11</li><li>12</li><li>13</li><li>14</li><li>15</li><li>16</li><li>17</li><li>18</li><li>19</li><li>20</li><li>21</li><li>22</li><li>23</li><li>24</li><li>25</li><li>26</li><li>27</li><li>28</li><li>29</li><li>30</li></ol>
  </section>

  <section class="month c1 r4"><h2>OCTOBER</h2>
    <ul class="weekdays"><li>S</li><li>M</li><li>T</li><li>W</li><li>T</li><li>F</li><li>S</li></ul>
    <ol class="days"><li class="s4">1</li><li>2</li><li>3</li><li>4</li><li>5</li><li>6</li><li>7</li><li>8</li><li>9</li><li>10</li><li>11</li><li>12</li><li>13</li><li>14</li><li>15</li><li>16</li><li>17</li><li>18</li><li>19</li><li>20</li><li>21</li><li>22</li><li>23</li><li>24</li><li>25</li><li>26</li><li>27</li><li>28</li><li>29</li><li>30</li><li>31</li></ol>
  </section>
  <section class="month c2 r4"><h2>NOVEMBER</h2>
    <ul class="weekdays"><li>S</li><li>M</li><li>T</li><li>W</li><li>T</li><li>F</li><li>S</li></ul>
    <ol class="days"><li>1</li><li>2</li><li>3</li><li>4</li><li>5</li><li>6</li><li>7</li><li>8</li><li>9</li><li>10</li><li>11</li><li>12</li><li>13</li><li>14</li><li>15</li><li>16</li><li>17</li><li>18</li><li>19</li><li>20</li><li>21</li><li>22</li><li>23</li><li>24</li><li>25</li><li>26</li><li>27</li><li>28</li><li>29</li><li>30</li></ol>
  </section>
  <section class="month c3 r4"><h2>DECEMBER</h2>
    <ul class="weekdays"><li>S</li><li>M</li><li>T</li><li>W</li><li>T</li><li>F</li><li>S</li></ul>
    <ol class="days"><li class="s2">1</li><li>2</li><li>3</li><li>4</li><li>5</li><li>6</li><li>7</li><li>8</li><li>9</li><li>10</li><li>11</li><li>12</li><li>13</li><li>14</li><li>15</li><li>16</li><li>17</li><li>18</li><li>19</li><li>20</li><li>21</li><li>22</li><li>23</li><li>24</li><li>25</li><li>26</li><li>27</li><li>28</li><li>29</li><li>30</li><li>31</li></ol>
  </section>

  <footer>
    <div class="brand">LN Warbeck</div>
    <div class="divider"></div>
    <p class="slogan">SAFETY<br>QUALITY<br>PRODUCTION</p>
    <div class="pill contact-pill">Contact Us</div>
    <ul class="info contact"><li>410 Ridge Street</li><li>Millbrook, WV 25990</li><li>Phone: 304.555.0142</li><li>Fax: 304.555.0187</li></ul>
    <div class="pill services-pill">Services</div>
    <ul class="info services"><li>- Natural Gas Distribution</li><li>- Natural Gas/Petroleum Transmission</li><li>- Water/Wastewater Systems and Facilities</li><li>- Facility Work</li><li>-&nbsp; Traffic control</li></ul>
  </footer>
</main>
</body>
</html>
```